brindlewood carpentry business card 2.0

id like to get some extra info added to my current business card ,but i am also open to a new design as well ,id like it to be a clean professional look
i have attached the original card files, i have also attached the ridgemark guild logo and licensed builder logo that id like to add to all the current info on the old card
also the color green is important as seen in the company logo

Industry/Entity Type

Carpentry

Colors
9bcb3c

```html
<!DOCTYPE html>
<html lang="en">
<head>
<meta charset="utf-8">
<title>Brindlewood Carpentry – Business Card</title>
<link rel="stylesheet" href="https://fonts.googleapis.com/css2?family=Arimo:wght@400;700&display=swap">
<style>
  :root {
    --stage: #2d2d2d;
    --brand-green: #9bcb3c;
    --card-white: #f7f7f7;
    --ink: #1c1c1c;
    --ink-soft: #3a3a3a;
    --rule: #222222;
    --badge-grey: #d9d9d9;
    --badge-navy: #2f4f8a;
  }
  * { box-sizing: border-box; margin: 0; padding: 0; }
  html, body {
    width: 1200px;
    height: 997px;
    overflow: hidden;
  }
  body {
    background: var(--stage);
    font-family: "Arimo", Arial, sans-serif;
    position: relative;
  }
  .card {
    position: absolute;
    top: 333px;
    width: 540px;
    height: 330px;
    overflow: hidden;
    box-shadow: 0 14px 30px rgba(0,0,0,0.45);
  }
  .card--front {
    left: 50px;
    background: var(--brand-green);
  }
  .card--back {
    left: 610px;
    background: var(--card-white);
  }
  .wordmark {
    position: absolute;
    display: flex;
    flex-direction: column;
    align-items: flex-end;
    color: var(--ink);
    font-weight: 400;
    line-height: 1;
  }
  .wordmark__name {
    font-size: 38px;
    letter-spacing: 1px;
  }
  .wordmark__trade {
    font-size: 17px;
    letter-spacing: 2px;
    margin-top: 4px;
  }
  .card--front .wordmark {
    left: 50%;
    top: 50%;
    transform: translate(-50%, -50%);
  }
  .card--back .wordmark {
    left: 50%;
    top: 62px;
    transform: translateX(-50%);
  }
  .card__rule {
    position: absolute;
    left: 168px;
    right: 28px;
    top: 196px;
    height: 1px;
    background: var(--rule);
  }
  .holder {
    position: absolute;
    left: 30px;
    top: 186px;
  }
  .holder__name {
    color: var(--brand-green);
    font-size: 17px;
    font-weight: 400;
  }
  .holder__role {
    color: var(--ink);
    font-size: 13px;
    margin-top: 3px;
  }
  .badges {
    position: absolute;
    right: 28px;
    top: 212px;
    display: flex;
    gap: 8px;
    align-items: center;
  }
  .badge--circle {
    width: 32px; height: 32px;
    border-radius: 50%;
    background: var(--badge-grey);
  }
  .badge--square {
    width: 30px; height: 30px;
    background: var(--badge-navy);
  }
  .contact {
    position: absolute;
    left: 30px;
    top: 240px;
    list-style: none;
  }
  .contact__item {
    display: flex;
    align-items: center;
    gap: 10px;
    font-size: 13px;
    color: var(--ink);
    height: 22px;
  }
  .contact__icon { width: 16px; height: 16px; flex: none; }
  .card__bands {
    position: absolute;
    left: 0; bottom: 0;
    width: 540px; height: 62px;
  }
  .web {
    position: absolute;
    right: 22px;
    bottom: 26px;
    color: #ffffff;
    font-size: 13px;
    font-weight: 700;
    letter-spacing: 0.3px;
  }
</style>
</head>
<body>

  <section class="card card--front" aria-label="Card front">
    <div class="wordmark">
      <span class="wordmark__name">BRINDLEWOOD</span>
      <span class="wordmark__trade">CARPENTRY</span>
    </div>
  </section>

  <section class="card card--back" aria-label="Card back">
    <div class="wordmark">
      <span class="wordmark__name">BRINDLEWOOD</span>
      <span class="wordmark__trade">CARPENTRY</span>
    </div>

    <div class="holder">
      <p class="holder__name">Graham Tully</p>
      <p class="holder__role">Director</p>
    </div>
    <div class="card__rule"></div>

    <div class="badges">
      <span class="badge badge--circle" role="img" aria-label="Licensed builder badge"></span>
      <span class="badge badge--square" role="img" aria-label="Ridgemark Guild member badge"></span>
    </div>

    <ul class="contact">
      <li class="contact__item">
        <svg class="contact__icon" viewBox="0 0 16 16" aria-hidden="true">
          <circle cx="8" cy="8" r="8" fill="#9bcb3c"/>
          <path d="M5 4.5c.6-.5 1.2-.4 1.5.2l.6 1.1c.2.4 0 .8-.3 1l-.4.3c.4.9 1.1 1.6 2 2l.3-.4c.3-.3.7-.4 1-.2l1.1.6c.6.3.7.9.2 1.5-.6.7-1.5.9-2.5.4-1.6-.8-2.9-2.1-3.7-3.7-.5-1-.3-1.9.2-2.8z" fill="#ffffff"/>
        </svg>
        <span>02104418260</span>
      </li>
      <li class="contact__item">
        <svg class="contact__icon" viewBox="0 0 16 16" aria-hidden="true">
          <circle cx="8" cy="8" r="8" fill="#9bcb3c"/>
          <rect x="4" y="5" width="8" height="6" rx="0.8" fill="none" stroke="#ffffff" stroke-width="1"/>
          <path d="M4.3 5.4L8 8.4l3.7-3" fill="none" stroke="#ffffff" stroke-width="1"/>
        </svg>
        <span>graham@brindlewoodcarpentry.co.nz</span>
      </li>
    </ul>

    <svg class="card__bands" viewBox="0 0 540 62" aria-hidden="true">
      <path d="M300 62 L300 30 Q300 12 322 12 L540 12 L540 62 Z" fill="#9bcb3c"/>
      <path d="M0 38 L292 38 Q300 38 300 30 L300 46 L0 46 Z" fill="#1c1c1c"/>
      <rect x="0" y="52" width="540" height="10" fill="#9bcb3c"/>
    </svg>
    <p class="web">www.brindlewoodcarpentry.co.nz</p>
  </section>

</body>
</html>
```